Bref créative
Tern Harbor Inc.
Professional
Dana Pellew
Owner
4817 Birchfield Rd.
Falls Church, VA 22041
dpellew@ternharborinc.example
www.ternharborinc.example
Would like to use logo from concurrent design effort

```html
<!DOCTYPE html>
<html lang="en">
<head>
<meta charset="utf-8">
<title>Tern Harbor Inc. Stationery</title>
<link href="https://fonts.googleapis.com/css2?family=Montserrat:wght@400;600;700&display=swap" rel="stylesheet">
<style>
:root{
  --stage:#3b3b3d;
  --paper:#ffffff;
  --ink:#2b2b33;
  --muted:#7a7a85;
  --red:#e1343b;
  --blue:#1f3f9f;
  --line:#d8d8de;
}
*{box-sizing:border-box;margin:0;padding:0}
html,body{width:1200px;height:310px;overflow:hidden}
body{background:var(--stage);font-family:"Montserrat",sans-serif;color:var(--ink);position:relative}
.piece{position:absolute;background:var(--paper);box-shadow:0 2px 6px rgba(0,0,0,.35)}
.brand{display:flex;align-items:center;gap:5px;font-weight:700;white-space:nowrap}
.brand .dot{border-radius:50%;background:var(--red);flex:none}

/* logo sheet */
.logo-block{position:absolute;left:14px;top:16px;color:#fff}
.logo-block .brand{font-size:21px;color:#fff}
.logo-block .brand .dot{width:18px;height:18px}
.logo-block .tagline{font-size:7px;margin:4px 0 0 23px;color:#ccc;letter-spacing:.5px}

/* cards */
.card{width:93px;height:54px;padding:7px}
.card .brand{font-size:9px}
.card .brand .dot{width:8px;height:8px}
.card-front{display:flex;align-items:center;justify-content:center}
.card-back{font-size:4px;line-height:1.5;color:var(--muted)}
.card-back .name{font-size:6px;font-weight:700;color:var(--ink)}
.card-back .role{font-size:4.5px;color:var(--red);margin-bottom:4px}
.card-blue{background:var(--blue);display:flex;align-items:center;justify-content:center}
.card-blue .brand{color:#fff}
.card-blue .brand .dot{background:#fff}
.card-back .top-rule{height:2px;background:var(--red);margin:-7px -7px 6px}

/* letterhead */
.letterhead{width:182px;height:288px;top:12px;padding:12px 12px}
.letterhead .head{display:flex;justify-content:space-between;align-items:flex-start}
.letterhead .brand{font-size:9px}
.letterhead .brand .dot{width:8px;height:8px}
.letterhead .contact{font-size:3.6px;line-height:1.6;color:var(--muted);text-align:right}
.letterhead .edge{position:absolute;left:0;top:0;bottom:0;width:2px;background:var(--blue)}
.letterhead .foot{position:absolute;bottom:10px;left:0;right:0;text-align:center;font-size:3.8px;color:var(--muted)}

/* envelope fronts */
.envelope{width:183px;height:87px;left:700px;padding:9px}
.envelope .brand{font-size:8px}
.envelope .brand .dot{width:7px;height:7px}
.envelope .sender{font-size:3.6px;color:var(--muted);line-height:1.6;margin-top:3px}
.envelope .recipient{position:absolute;left:78px;top:44px;font-size:4.2px;line-height:1.7;color:var(--ink)}
.envelope .foot{position:absolute;bottom:6px;left:9px;font-size:3.6px;color:var(--muted)}

/* stacked envelopes */
.stack{position:absolute;left:924px;top:108px;width:206px;height:160px}
.stack svg{position:absolute;left:0;top:0}
</style>
</head>
<body>

<div class="logo-block">
  <div class="brand"><span class="dot"></span>Tern Harbor Inc.</div>
  <div class="tagline">Professional</div>
</div>

<div class="piece card card-front" style="left:10px;top:96px">
  <div class="brand"><span class="dot"></span>Tern Harbor Inc.</div>
</div>
<div class="piece card card-back" style="left:106px;top:96px">
  <div class="top-rule"></div>
  <div class="name">Dana Pellew</div>
  <div class="role">Owner</div>
  <div>4817 Birchfield Rd.</div>
  <div>Falls Church, VA 22041</div>
  <div>dpellew@ternharborinc.example</div>
  <div>www.ternharborinc.example</div>
</div>
<div class="piece card card-front" style="left:10px;top:156px">
  <div class="brand"><span class="dot"></span>Tern Harbor Inc.</div>
</div>
<div class="piece card card-blue" style="left:106px;top:156px">
  <div class="brand"><span class="dot"></span>Tern Harbor Inc.</div>
</div>

<div class="piece letterhead" style="left:269px">
  <span class="edge"></span>
  <div class="head">
    <div class="brand"><span class="dot"></span>Tern Harbor Inc.</div>
    <div class="contact">4817 Birchfield Rd.<br>Falls Church, VA 22041<br>dpellew@ternharborinc.example</div>
  </div>
  <div class="foot">www.ternharborinc.example</div>
</div>
<div class="piece letterhead" style="left:468px">
  <span class="edge"></span>
  <div class="head">
    <div class="brand"><span class="dot"></span>Tern Harbor Inc.</div>
    <div class="contact">4817 Birchfield Rd.<br>Falls Church, VA 22041<br>dpellew@ternharborinc.example</div>
  </div>
  <div class="foot">www.ternharborinc.example</div>
</div>

<div class="piece envelope" style="top:100px">
  <div class="brand"><span class="dot"></span>Tern Harbor Inc.</div>
  <div class="sender">4817 Birchfield Rd.<br>Falls Church, VA 22041</div>
  <div class="recipient">Recipient Name<br>Street Address Line<br>City, State ZIP</div>
  <div class="foot">www.ternharborinc.example</div>
</div>
<div class="piece envelope" style="top:192px">
  <div class="brand"><span class="dot"></span>Tern Harbor Inc.</div>
  <div class="sender">4817 Birchfield Rd.<br>Falls Church, VA 22041</div>
  <div class="recipient">Recipient Name<br>Street Address Line<br>City, State ZIP</div>
  <div class="foot">www.ternharborinc.example</div>
</div>

<div class="stack">
  <svg width="206" height="160" viewBox="0 0 206 160">
    <rect x="4" y="0" width="200" height="66" fill="var(--red)"/>
    <polygon points="4,0 104,40 204,0" fill="#c72a31"/>
    <rect x="2" y="38" width="200" height="66" fill="var(--blue)"/>
    <polygon points="2,38 102,78 202,38" fill="#183384"/>
    <rect x="0" y="76" width="200" height="80" fill="var(--paper)"/>
    <polyline points="0,76 100,118 200,76" fill="none" stroke="var(--line)" stroke-width="1"/>
  </svg>
</div>

</body>
</html>
```